Online Psychiatry business - Business Card

I need a business card design. The target audience is busy professionals of any field (this therapy appeals best to 24-35 year olds). It involves psychiatry by tele-medicine (or video-conference). Nothing on it should be a giveaway that it's about mental health. Professional design with silver or gold as the primary colors appeals to me. The card must be as simple and as uncluttered as possible. Some color and flowing design on the edge of the card appeals to me.
CrestLumaCareNet.com should probably appear in the center of the card and stand out, i.e. bold lettering, and easy to read, no cursive, but Ariel Black. Some where below this, should appear "Too Busy to Take Care of Yourself? Think again." Since this isn't office based, I don't think an office address is necessary and limits clutter.
Information that does need to appear is my name: Gerald Mewkinson, MD
General phone number: 618-472-9086. I'm hoping to get an 24-hour answering service soon so leave a little room for this. In addition I want to include two email addresses:
CrestLumaCareNet@mailvora.com and CrestLumaCare247@mailvora.com
Updates

I like the designs. I would like someone to put the website in bold in the center

 as most have been doing with a smaller font reminder nearby saying "No time" etc.
but I'd like to put my name down in the corner with the rest of the contact material.
Black print against a white or grey background appeals to me, with darker silver artwork near the sides (simple abstract, like wavy lines or something you can one up with that works. 
thanks

I ve tried to provide as much feedback as possible given my time limits, so if you have extra questions, please feel free to email. I tried to attach a file of a business card I really like but make be difficult to actually manufacture. I'm going to send you a link to the photo. The card has a pull tab. There is not much information on the outside. In fact, if you were to design the outside, I would just print : Too Busy to Take Care of Yourself? Think Again.

When you pull the tab the remaining information is on the bottom half of the card. Please don't use the color pink!!!!
http://www.printfolkgallery.net/2009/05/100-really-creative-business-cards/
It is the 39th photo on the list, about 2/3ds of the way down the page. It is titled: Ruvelinkiste

#7 and #16 have an appeal to me, except for the dot patterns
Hope this helps

I'm running out of time and energy. I 've been trying to give do down the list and give  individual feedback but I won't be able to do that anymore.

So if you have any specific questions, write me, and again thank you for all your effort!!

I know i received your files, including your zip files, Tolkra,

but Milos, did you send me the files including ZIP on project 5139624?
thanks

Target Market(s)

Working professionals and executive, attorneys, etc.

Industry/Entity Type

Business

Logo Text

Don't Have Time to Take Care of Yourself? Think Again.

Logo styles of interest
Pictorial/Combination Logo
Wordmark Logo
Font styles to use
Other font styles liked:
• Ariel Black appeals to me the most

Requirements
Must have
• Want to emphasize that the website must be obvious, easily found (The CrestLumaCareNet.com)
For that reason i'd like the card to be white, and minimal decoration on one or both sides just to add some style and color
Nice to have
• A Very uncluttered, elegant design, and something that makes it stick in your head-doesn't everyone want the last?
Should not have
• Nothing on the card that give it away that this is about psychiatry, such as brain or other symbol, but also nothing that gives it away as a medical business, such as a stethoscope or red cross or anything.

```html
<!DOCTYPE html>
<html lang="en">
<head>
<meta charset="utf-8">
<title>CrestLumaCareNet.com – Business Card</title>
<link rel="stylesheet" href="https://fonts.googleapis.com/css2?family=Archivo+Black&family=Arimo:wght@700&display=swap">
<style>
  :root {
    --ink: #1a1a1a;
    --paper: #ffffff;
    --edge: #9a9a9a;
    --band: #dedede;
    --pattern-light: #f7f7f7;
    --pattern-mid: #ececec;
  }
  html, body {
    margin: 0;
    padding: 0;
    width: 1200px;
    height: 704px;
    overflow: hidden;
    background: var(--paper);
  }
  .card {
    position: relative;
    width: 1200px;
    height: 704px;
    box-sizing: border-box;
    border: 2px solid var(--edge);
    background: var(--paper);
    color: var(--ink);
    font-family: "Arimo", Arial, sans-serif;
    font-weight: 700;
  }
  .top-pattern {
    position: absolute;
    left: 0;
    top: 0;
    width: 100%;
    height: 60px;
    background: linear-gradient(180deg, var(--pattern-mid) 0%, var(--pattern-light) 55%, var(--paper) 100%);
  }
  .website {
    position: absolute;
    left: 52px;
    top: 170px;
    margin: 0;
    font-family: "Archivo Black", "Arial Black", sans-serif;
    font-weight: 400;
    font-size: 84px;
    line-height: 1;
    letter-spacing: 0.5px;
  }
  .tagline {
    position: absolute;
    right: 106px;
    top: 288px;
    margin: 0;
    font-size: 19px;
    line-height: 1;
  }
  .contact {
    position: absolute;
    left: 38px;
    top: 370px;
  }
  .contact__name {
    margin: 0;
    font-size: 34px;
    line-height: 1;
  }
  .contact__title {
    margin: 8px 0 0 4px;
    font-size: 18px;
    line-height: 1;
  }
  .contact__phone {
    margin: 18px 0 0;
    font-size: 27px;
    line-height: 1;
  }
  .divider-band {
    position: absolute;
    left: 0;
    top: 598px;
    width: 100%;
    height: 27px;
    background: var(--band);
  }
  .emails {
    position: absolute;
    left: 44px;
    right: 40px;
    top: 648px;
    display: flex;
    justify-content: space-between;
    font-size: 26.5px;
    line-height: 1;
  }
</style>
</head>
<body>
  <div class="card">
    <div class="top-pattern" role="img" aria-label="Soft band of light grey tiled squares along the top edge"></div>

    <h1 class="website">CrestLumaCareNet.com</h1>
    <p class="tagline">"Too Busy to Take Care of Yourself? Think again."</p>

    <div class="contact">
      <p class="contact__name">Gerald Mewkinson</p>
      <p class="contact__title">MD</p>
      <p class="contact__phone">Phone : 618-472-9086</p>
    </div>

    <div class="divider-band"></div>

    <div class="emails">
      <span class="emails__item">CrestLumaCareNet@mailvora.com</span>
      <span class="emails__item">CrestLumaCare247@mailvora.com</span>
    </div>
  </div>
</body>
</html>
```